we need 5 posters for our restaurant. the posters will be based on a design template which I will provide in various formats. I will also provide the photos for the posters. so basically all that needs to be done is swapping over the photo from the current template and changing the price and menu item name to match the photo. we need 5 of these.

```html
<!DOCTYPE html>
<html lang="en">
<head>
<meta charset="utf-8">
<title>Classic Burger – Poster Draft</title>
<link rel="stylesheet" href="https://fonts.googleapis.com/css2?family=Montserrat:wght@800&family=Fredoka:wght@600&family=Caveat+Brush&family=Kaushan+Script&display=swap">
<style>
  :root {
    --page-bg: #e6e2e7;
    --note-ink: #0b0b0b;
    --poster-white: #ffffff;
    --sky-blue: #38ade4;
    --royal-blue: #1558a6;
    --script-blue: #2158a8;
  }
  * { margin: 0; padding: 0; box-sizing: border-box; }
  html, body {
    width: 1200px;
    height: 1200px;
    overflow: hidden;
    background: var(--page-bg);
  }
  .canvas {
    position: relative;
    width: 1200px;
    height: 1200px;
  }
  .draft-note {
    position: absolute;
    top: 136px;
    left: 0;
    width: 1200px;
    text-align: center;
    font-family: "Montserrat", sans-serif;
    font-weight: 800;
    font-size: 37px;
    line-height: 42px;
    letter-spacing: 2.6px;
    color: var(--note-ink);
  }
  .draft-note .line-one { display: block; padding-right: 24px; }
  .draft-note .line-two { display: block; letter-spacing: 2.2px; }

  .poster {
    position: absolute;
    left: 355px;
    top: 337px;
    width: 491px;
    height: 703px;
    background: var(--poster-white);
    overflow: hidden;
  }
  .poster-art {
    position: absolute;
    inset: 0;
    width: 491px;
    height: 703px;
  }
  .poster-title {
    position: absolute;
    left: 38px;
    top: 22px;
    width: 260px;
    font-family: "Kaushan Script", cursive;
    font-weight: 400;
    color: var(--script-blue);
    transform: rotate(-8deg);
    transform-origin: left top;
    -webkit-text-stroke: 1px var(--poster-white);
  }
  .poster-title .word-one {
    display: block;
    font-size: 86px;
    line-height: 90px;
    padding-left: 14px;
  }
  .poster-title .word-two {
    display: block;
    font-size: 104px;
    line-height: 104px;
    margin-top: -12px;
  }
  .price-badge {
    position: absolute;
    left: 19px;
    top: 536px;
    width: 136px;
    height: 136px;
    border-radius: 50%;
    background: var(--poster-white);
    box-shadow: inset 0 0 0 2px var(--royal-blue);
    display: flex;
    flex-direction: column;
    align-items: center;
    justify-content: center;
    font-family: "Caveat Brush", cursive;
    color: var(--script-blue);
    font-size: 29px;
    line-height: 28px;
    text-align: center;
    transform: rotate(-14deg);
  }
  .tagline {
    position: absolute;
    left: 180px;
    top: 576px;
    width: 295px;
    text-align: center;
    font-family: "Fredoka", sans-serif;
    font-weight: 600;
    color: var(--poster-white);
    text-transform: uppercase;
  }
  .tagline .lead {
    display: block;
    font-size: 34px;
    line-height: 38px;
    letter-spacing: 1px;
  }
  .tagline .hero {
    display: block;
    font-size: 66px;
    line-height: 62px;
    letter-spacing: 2px;
    margin-top: 4px;
  }
</style>
</head>
<body>
<main class="canvas">
  <p class="draft-note">
    <span class="line-one">THIS IS JUST TEH FIRST DRAFT</span>
    <span class="line-two">I NEED PRICES SO I CAN FINISH THE DESIGNS</span>
  </p>

  <section class="poster">
    <svg class="poster-art" viewBox="0 0 491 703" xmlns="http://www.w3.org/2000/svg">
      <defs>
        <linearGradient id="photo-tones" x1="0" y1="0" x2="0" y2="1">
          <stop offset="0" stop-color="#dfe6e8"/>
          <stop offset="0.22" stop-color="#e6c08c"/>
          <stop offset="0.5" stop-color="#c9652d"/>
          <stop offset="0.75" stop-color="#e2b27a"/>
          <stop offset="1" stop-color="#d8bd96"/>
        </linearGradient>
        <linearGradient id="photo-fade-top" x1="0" y1="0" x2="0" y2="1">
          <stop offset="0" stop-color="#38ade4"/>
          <stop offset="1" stop-color="#38ade4" stop-opacity="0"/>
        </linearGradient>
        <linearGradient id="photo-fade-bottom" x1="0" y1="0" x2="0" y2="1">
          <stop offset="0" stop-color="#38ade4" stop-opacity="0"/>
          <stop offset="1" stop-color="#38ade4"/>
        </linearGradient>
      </defs>

      <path class="brush-band" fill="var(--sky-blue)"
        d="M0 214 L30 210 L60 218 L100 206 L140 214 L180 204 L220 208 L250 196 L290 172 L325 168 L355 146 L385 142 L410 128 L440 132 L465 122 L491 114 L491 300 L0 300 Z"/>

      <g role="img" aria-label="Photo of a crispy fried chicken burger with slaw and hot sauce on a soft bun, on a wooden table with a side salad bowl">
        <rect x="0" y="232" width="491" height="320" fill="url(#photo-tones)"/>
        <rect x="0" y="232" width="491" height="28" fill="url(#photo-fade-top)"/>
        <rect x="0" y="500" width="491" height="52" fill="url(#photo-fade-bottom)"/>
      </g>

      <path class="base-band" fill="var(--royal-blue)"
        d="M0 590 L20 584 L40 572 L70 566 L100 560 L130 556 L170 552 L210 548 L250 546 L290 542 L330 540 L370 534 L410 534 L450 528 L491 526 L491 703 L0 703 Z"/>
    </svg>

    <h2 class="poster-title">
      <span class="word-one">Classic</span>
      <span class="word-two">Burger</span>
    </h2>

    <div class="price-badge">
      <span>COAST</span>
      <span>BURGER</span>
      <span>9.90</span>
    </div>

    <h1 class="tagline">
      <span class="lead">Classics for a</span>
      <span class="hero">Reason</span>
    </h1>
  </section>
</main>
</body>
</html>
```